Flyer-Design für Sabine Wellrath Coaching für Führungskräfte
Zielgruppe
Coaching für Führungskräfte, Seminare für Führungskräfte.
Zielgruppe: Führungskräfte, Unternehmer, Geschäftsführer, Vorstände
Aufgabenstellung
Mein Logo soll beibehalten werden. Es soll ein vierseitiger Flyer sein, der meine Leistungen beschreibt. Es soll sehr modern sein (Stichwort: digital leadership) und seriös. Möglichst nicht das übliche Format, aber nicht zu groß.
Der Text soll weitgehend aus meiner Homepage (www.coaching-wellrath-beispiel.de) übernommen werden, aber es sollen auch zusätzlich Seminare aufgeführt werden.
Bis auf das Logo müssen die angehängten Dateien nicht unbedingt verwendet werden.

```html
<!DOCTYPE html>
<html lang="de">
<head>
<meta charset="utf-8">
<title>Sabine Wellrath – Coaching und Mediation</title>
<link href="https://fonts.googleapis.com/css2?family=Source+Sans+3:ital,wght@0,300;0,400;0,600;1,300&display=swap" rel="stylesheet">
<style>
  :root {
    --backdrop: #808080;
    --paper: #ffffff;
    --ink: #1c1c1c;
    --accent: #c8105e;
    --navy: #1f3a6b;
    --photo-blue: #2a6a9c;
    --photo-light: #c9dbe8;
  }
  * { margin: 0; padding: 0; box-sizing: border-box; }
  html, body { width: 1200px; height: 1200px; overflow: hidden; }
  body {
    background: var(--backdrop);
    font-family: "Source Sans 3", "Source Sans Pro", sans-serif;
    color: var(--ink);
    position: relative;
  }
  .spread {
    position: absolute;
    left: 15px; top: 184px;
    width: 1171px; height: 830px;
    background: var(--paper);
  }
  .portrait {
    position: absolute;
    left: 48px; top: 140px;
    width: 191px; height: 243px;
    border: 1px solid #d6d6d6;
    background: linear-gradient(160deg, #f4f1ee 0%, #d9b98f 45%, #8a8a8e 100%);
  }
  .motto {
    position: absolute;
    left: 48px; top: 416px;
    width: 210px;
    font-weight: 300;
    font-size: 19.5px;
    line-height: 30.8px;
    color: var(--navy);
  }
  .motto .signature {
    display: block;
    margin-top: 6px;
    font-style: italic;
  }
  .headline {
    position: absolute;
    left: 300px; top: 132px;
    font-weight: 400;
    font-size: 23px;
    color: var(--accent);
  }
  .column {
    position: absolute;
    width: 262px;
    font-size: 12.3px;
    line-height: 22.3px;
    font-weight: 400;
  }
  .column p + p { margin-top: 22.3px; }
  .column .lead { font-weight: 600; }
  .column .contact { font-weight: 600; color: var(--navy); }
  .col-coaching { left: 300px; top: 192px; }
  .col-mediation { left: 605px; top: 415px; }
  .col-closing { left: 885px; top: 415px; }
  .scene-photo {
    position: absolute;
    left: 605px; top: 141px;
    width: 546px; height: 241px;
    background: linear-gradient(115deg, var(--photo-blue) 0%, var(--photo-light) 45%, var(--photo-blue) 70%, #7fa6c4 100%);
  }
</style>
</head>
<body>
  <section class="spread">
    <div class="portrait" role="img" aria-label="Porträtfoto der Coachin Sabine Wellrath"></div>

    <blockquote class="motto">
      In jedem Menschen steckt alles Nötige, um ein glückliches und erfolgreiches Leben zu führen.
      <span class="signature">Sabine Wellrath</span>
    </blockquote>

    <h1 class="headline">Coaching und Mediation</h1>

    <div class="column col-coaching">
      <p>Sie suchen individuelle Lösungen für Konflikt&shy;situationen oder berufliche Herausforderungen mit der Hilfe von Coaching oder Mediation? Als Coach und Mediatorin mit langjähriger, eigener Erfahrung als Führungskraft, unterstütze ich hierbei Privatpersonen, Führungskräfte und Unternehmen. Gemeinsam machen wir uns an die Arbeit und entwickeln Wege zur Verwirkli&shy;chung Ihrer persönlichen Ziele!</p>
      <p class="lead">Mein Business Coaching-Angebot richtet sich an Personen mit Führungsverantwortung und/oder im Management und an Unternehmen.</p>
      <p>Der Führungsstil hat einen erheblichen Einfluss auf den Erfolg einer Organisation. Eine gute Füh&shy;rung der Mitarbeiter sorgt in der Regel für Zufrie&shy;denheit, Motivation und Engagement. Dies wirkt sich wiederum positiv auf die Kundenzufrieden&shy;heit aus. Somit sollten Sie für Ihren beruflichen Weg über ein Coaching nachdenken, denn schon eine kleine Veränderung im Führungsstil kann Ihren Mitarbeitern mehr entlocken. Mit meinem Training können Sie Ihre Führungskompetenz stärken und/oder neue Stärken entwickeln.</p>
    </div>

    <div class="scene-photo" role="img" aria-label="Blau getöntes Foto: zwei Kletterer sichern sich gegenseitig am Fels"></div>

    <div class="column col-mediation">
      <p class="lead">Mein Angebot für Mediation richtet sich an Konfliktparteien, die an einer konstruktiven Beilegung interessiert sind.</p>
      <p>Menschen brauchen soziale Beziehungen, um ein zufriedenes oder glückliches Leben führen zu können. Beziehungen und arbeiten im Team bedeutet aber immer auch zumindest mögliche Konflikte. Konflikte können im Nachhinein als Bereicherung wahrgenommen werden, an denen der Mensch wächst. Im gegenwärtigen Erleben kann ein Konflikt unlösbar erscheinen und Kraft binden. Es kann dann hilfreich sein, sich bei der Lösung des Konfliktes Hilfe zu suchen. Um zu einer Lösung zu finden, bei der es keine Verlierer</p>
    </div>

    <div class="column col-closing">
      <p>gibt, biete ich Ihnen Mediation an. Hierbei nehme ich mir Zeit, um mit meinem geschulten Blick von Aussen eine Lösung zu finden, bei der Ihre eigenen Ziele und die der anderen Partei berück&shy;sichtigt werden.</p>
      <p class="contact">Bei Fragen oder Interesse an einer Beratung schreiben Sie mir per Mail oder rufen Sie mich direkt an unter 0170 4829163. Gerne können wir Termine vereinbaren, ich freue mich auf Sie!</p>
    </div>
  </section>
</body>
</html>
```